New Property management company business cards

Looking for a new business card, to reflect new younger ownership
Card should be clean, simple and professional but with a modern layout that is conveys our new logo and business model

Key aspects of the business:

Property Management
Facility Maintenance
Project Management
Tenant Improvements

Mailing Address:
PO BOX 7186
Harlow CA, 95368

Phone: 209-614-8837
Direct: 209-614-8831

Doyle Farrant
President

Target Market(s)

Commercial property owners

Industry/Entity Type

Real Estate property management

Contact Information for Business Card

Open to all designs but lean toward vertical layouts

Requirements
Must have
• Logo and space to customize name and contact info

```html
<!DOCTYPE html>
<html lang="en">
<head>
<meta charset="utf-8">
<title>Corvane Property Management – Business Cards</title>
<link rel="stylesheet" href="https://fonts.googleapis.com/css2?family=Montserrat:wght@500;600&family=Questrial&display=swap">
<style>
  :root {
    --backdrop: #d1d2d4;
    --card: #ffffff;
    --ink: #34333f;
    --teal: #22aca9;
  }
  * { margin: 0; padding: 0; box-sizing: border-box; }
  html, body { width: 1200px; height: 1199px; overflow: hidden; }
  body { background: var(--backdrop); position: relative; font-family: "Questrial", sans-serif; color: var(--ink); }

  .card { position: absolute; left: 174px; width: 852px; height: 487px; background: var(--card); overflow: hidden; }
  .card--front { top: 82px; }
  .card--back { top: 630px; }

  .accent-dark { position: absolute; left: 0; top: 0; width: 351px; height: 234px; background: var(--ink); }
  .accent-teal { position: absolute; left: 0; top: 234px; width: 213px; height: 253px; background: var(--teal); }

  .brand { position: absolute; text-align: center; font-family: "Montserrat", sans-serif; font-weight: 600; color: var(--ink); white-space: nowrap; }
  .brand__mark { display: block; margin: 0 auto; background: var(--teal); }
  .brand__name { display: block; }
  .brand__tag { display: block; line-height: 1; }

  .card--front .brand { left: 472px; top: 60px; width: 360px; }
  .card--front .brand__mark { width: 44px; height: 44px; margin-bottom: 18px; }
  .card--front .brand__name { font-size: 37px; line-height: 1.1; letter-spacing: 0.14em; padding-left: 0.14em; }
  .card--front .brand__tag { font-size: 10px; letter-spacing: 0.56em; padding-left: 0.56em; }

  .card--back .brand { left: 333px; top: 150px; width: 520px; }
  .card--back .brand__mark { width: 64px; height: 64px; margin-bottom: 58px; }
  .card--back .brand__name { font-size: 56px; line-height: 1.1; letter-spacing: 0.17em; padding-left: 0.17em; }
  .card--back .brand__tag { font-size: 19px; margin-top: 4px; letter-spacing: 0.44em; padding-left: 0.44em; }

  .person { position: absolute; left: 419px; top: 217px; }
  .person__name { font-family: "Montserrat", sans-serif; font-weight: 600; font-size: 39px; line-height: 1; letter-spacing: -0.01em; white-space: nowrap; }
  .person__role { display: flex; align-items: center; gap: 4px; margin-top: 0; color: var(--teal); font-size: 24px; line-height: 1; }
  .person__role::after { content: ""; display: block; width: 131px; height: 2px; background: var(--teal); }

  .phone { position: absolute; left: 330px; top: 325px; display: flex; gap: 20px; align-items: center; }
  .phone__icon { width: 22px; height: 22px; }
  .phone__list { font-size: 14.5px; line-height: 18px; letter-spacing: 0.14em; }

  .mailing { position: absolute; left: 330px; top: 391px; }
  .section-title { color: var(--teal); font-size: 19px; letter-spacing: 0.09em; line-height: 1; white-space: nowrap; }
  .mailing address { font-style: normal; font-size: 14px; line-height: 18px; letter-spacing: 0.12em; margin-top: 13px; white-space: nowrap; }

  .services { position: absolute; left: 573px; top: 328px; }
  .services .section-title { font-size: 21px; letter-spacing: 0.08em; }
  .services ul { list-style: none; margin-top: 20px; font-size: 16px; line-height: 19.3px; letter-spacing: 0.09em; white-space: nowrap; }
  .services li::before { content: "•"; font-size: 10px; margin-right: 2px; vertical-align: 2px; }
</style>
</head>
<body>
  <section class="card card--front" aria-label="Business card front">
    <div class="accent-dark"></div>
    <div class="accent-teal"></div>

    <div class="brand">
      <span class="brand__mark"></span>
      <span class="brand__name">CORVANE</span>
      <span class="brand__tag">PROPERTY MANAGEMENT</span>
    </div>

    <div class="person">
      <h1 class="person__name">DOYLE FARRANT</h1>
      <p class="person__role">PRESIDENT</p>
    </div>

    <div class="phone">
      <svg class="phone__icon" viewBox="0 0 24 24" aria-hidden="true">
        <path fill="var(--teal)" d="M6.6 2.5c.8-.5 1.6-.2 2 .6l1.4 3c.3.7.1 1.4-.5 1.8l-1.3.9c.9 2.6 3 4.9 5.7 6.2l1-1.2c.5-.6 1.2-.7 1.9-.4l3 1.6c.7.4 1 1.2.5 2l-1 1.6c-.7 1.1-2 1.6-3.3 1.2C9.6 18.4 5 13.6 3.8 7.3c-.2-1.2.2-2.4 1.2-3.1z"/>
      </svg>
      <div class="phone__list">
        <p>209-614-8837</p>
        <p>209-614-8831</p>
      </div>
    </div>

    <div class="mailing">
      <p class="section-title">Mailing Address:</p>
      <address>PO BOX 7186<br>HARLOW CA, 95368</address>
    </div>

    <div class="services">
      <p class="section-title">SERVICES:</p>
      <ul>
        <li>PROPERTY MANAGEMENT</li>
        <li>FACILITY MAINTENANCE</li>
        <li>PROJECT MANAGEMENT</li>
        <li>TENANT IMPROVEMENTS</li>
      </ul>
    </div>
  </section>

  <section class="card card--back" aria-label="Business card back">
    <div class="accent-dark"></div>
    <div class="accent-teal"></div>

    <div class="brand">
      <span class="brand__mark"></span>
      <span class="brand__name">CORVANE</span>
      <span class="brand__tag">PROPERTY MANAGEMENT</span>
    </div>
  </section>
</body>
</html>
```